Learn-to-Swim Program for Children's Day Camp (Walter Brightley Fieldgrounds)

We are a children's camp with a robust swim instruction program and we need a series of 5 kid-friendly banners which list the skills learned in our swim program that can be hung up around each outdoor pool complex. All together there are 6 overarching levels and 12 sublevels (see attached). Except for the Level V & VI, each banner should be one overarching level and the 2-3 sublevels that define it.

Each swim level has a name, most of which are sea creatures, and we want to have a corresponding image/avatar to go with the swim level name (e.g. tadpole, barracuda, orca, goldfish, catfish).

The banners should be 3 feet (width) by 5 feet (height). The banners will be hung outdoors so it needs a color scheme that won't get lost in the sunlight.

We will want to include our logo but do not need the design to match our logo colors. Logo can be in black or white.

Our website is: www.campwbf.example

Target Market(s)

children age 5 - 12

Industry/Entity Type

children's day camp

Requirements
Must have
• A progression from level I to level VI. Should have a happy, bright, fun, tone, text MUST be legible from at least a 5 foot distance
Should not have
• adult themes, a scheme that evokes sadness or fear

```html
<!DOCTYPE html>
<html lang="en">
<head>
<meta charset="utf-8">
<title>Walter Brightley Fieldgrounds – Swim Level Banners</title>
<link rel="stylesheet" href="https://fonts.googleapis.com/css2?family=Bungee&family=Oswald:wght@400;500&family=Arimo:wght@700&display=swap">
<style>
  :root{
    --orange:#f8671c;
    --teal:#00bab1;
    --yellow:#f3e83b;
    --white:#ffffff;
    --ink:#1c1c1c;
    --page:#ffffff;
  }
  *{box-sizing:border-box;margin:0;padding:0}
  html,body{width:1135px;height:1200px;overflow:hidden;background:var(--page)}
  .sheet{position:relative;width:1135px;height:1200px}
  .banner{position:absolute;width:318px;height:530px;background:var(--orange);overflow:hidden}
  .banner-bg{position:absolute;inset:0;width:318px;height:530px}
  .brand{position:absolute;top:32px;left:0;width:318px;display:flex;justify-content:center;align-items:center;gap:5px}
  .brand-square{width:11px;height:11px;background:var(--white)}
  .brand-name{font:500 7.5px/1 "Oswald",sans-serif;color:var(--white);text-transform:uppercase;letter-spacing:.6px}
  .tier{position:absolute;left:18px}
  .tier-name{font:20px/1 "Bungee",sans-serif;color:var(--yellow);letter-spacing:1.5px;display:inline-block;padding-bottom:2px;border-bottom:1.5px solid var(--yellow)}
  .skills{list-style:none;margin:10px 0 0 9px}
  .skills li{position:relative;padding-left:19px;font:400 9.3px/11px "Oswald",sans-serif;color:var(--yellow);text-transform:uppercase;margin-bottom:3.6px}
  .skills li::before{content:"";position:absolute;left:0;top:1.5px;width:7px;height:7px;border:1px solid var(--yellow);border-radius:50%}
  .skills li::after{content:"";position:absolute;left:2.2px;top:4.6px;width:3px;height:1px;background:var(--yellow)}
  .skills.compact{margin-top:8px}
  .skills.compact li{font-size:7px;line-height:9px;margin-bottom:2.4px;padding-left:15px}
  .skills.compact li::before{width:6px;height:6px;top:1.4px}
  .skills.compact li::after{left:1.8px;top:4px}
  .move-up{position:absolute;display:flex;align-items:flex-start;gap:8px}
  .move-up-tag{flex:none;width:36px;height:15px;background:var(--yellow);clip-path:polygon(0 0,76% 0,76% -10%,100% 50%,76% 110%,76% 100%,0 100%);font:700 7px/15px "Arimo",sans-serif;color:var(--ink);padding-left:3px;letter-spacing:-.2px}
  .move-up-text{font:700 9.5px/12.3px "Arimo",sans-serif;color:var(--white)}
  .move-up.side{gap:5px}
  .move-up.side .move-up-text{font-size:6.8px;line-height:9.8px;width:80px}
  .art{position:absolute;border-radius:40% 55% 45% 50%}
</style>
</head>
<body>
<main class="sheet">

  <!-- Level I : Wader / Splasher -->
  <section class="banner" style="left:71px;top:53px">
    <svg class="banner-bg" viewBox="0 0 318 530" aria-hidden="true">
      <path d="M0 0H318V2C250 58 205 72 159 72C105 72 55 50 0 4Z" fill="var(--teal)"/>
      <path d="M0 8C55 55 108 78 159 78C208 78 255 58 318 6" fill="none" stroke="var(--yellow)" stroke-width="3"/>
      <path d="M318 225V300H200Z" fill="var(--teal)"/>
      <path d="M0 288V345L68 312Z" fill="var(--teal)"/>
      <path d="M0 312C140 305 250 270 318 218" fill="none" stroke="var(--yellow)" stroke-width="5"/>
      <path d="M90 530C130 505 200 505 260 530Z" fill="var(--yellow)"/>
    </svg>
    <div class="brand"><span class="brand-square"></span><span class="brand-name">Walter Brightley Fieldgrounds</span></div>

    <div class="art" role="img" aria-label="Illustration of a stork standing on a rock in a pond" style="left:220px;top:71px;width:78px;height:133px;background:linear-gradient(180deg,#f4efe6,#9fc9c4 70%,#7a8a8d)"></div>
    <div class="tier" style="top:78px">
      <h2 class="tier-name">Wader</h2>
      <ul class="skills" style="width:170px">
        <li>Gets into the water with assistance</li>
        <li>Follows pool rules</li>
        <li>Can hold big breath and get chin/ cheeks in water</li>
        <li>Cups hands to hold water and get some of face wet</li>
        <li>Doesn't always need assistance in water</li>
      </ul>
    </div>
    <div class="move-up" style="left:26px;top:256px"><span class="move-up-tag">Move-Up</span><p class="move-up-text">Must be comfortable<br>entering the water</p></div>

    <div class="art" role="img" aria-label="Illustration of a child in a swim cap splashing in the water" style="left:153px;top:312px;width:158px;height:52px;background:linear-gradient(90deg,#2fc2b8,#f3f3f3)"></div>
    <div class="tier" style="top:344px">
      <h2 class="tier-name">Splasher</h2>
      <ul class="skills" style="width:280px">
        <li>Enters and exits pool without assistance</li>
        <li>Can do a slide in entry</li>
        <li>Plays in water up to chest deep</li>
        <li>Dips face and head in water</li>
        <li>Blows bubbles through the mouth</li>
      </ul>
    </div>
    <div class="move-up" style="left:26px;top:476px"><span class="move-up-tag">Move-Up</span><p class="move-up-text">Must fully submerge body and head<br>underwater (no nose holding)</p></div>
  </section>

  <!-- Level II : Guppy / Tadpole -->
  <section class="banner" style="left:407px;top:53px">
    <svg class="banner-bg" viewBox="0 0 318 530" aria-hidden="true">
      <path d="M0 0H318V2C250 58 205 72 159 72C105 72 55 50 0 4Z" fill="var(--teal)"/>
      <path d="M0 8C55 55 108 78 159 78C208 78 255 58 318 6" fill="none" stroke="var(--yellow)" stroke-width="3"/>
      <path d="M318 230V310H230Z" fill="var(--teal)"/>
      <path d="M0 275C60 300 150 300 240 260" fill="none" stroke="var(--yellow)" stroke-width="3"/>
      <path d="M0 268V330L38 300Z" fill="var(--teal)"/>
      <path d="M0 340C200 340 250 300 318 218" fill="none" stroke="var(--yellow)" stroke-width="5"/>
      <path d="M90 530C130 505 200 505 260 530Z" fill="var(--yellow)"/>
    </svg>
    <div class="brand"><span class="brand-square"></span><span class="brand-name">Walter Brightley Fieldgrounds</span></div>

    <div class="art" role="img" aria-label="Illustration of an orange guppy with a spotted tail" style="left:207px;top:65px;width:100px;height:79px;background:linear-gradient(135deg,#ff8a4a,#c2571b)"></div>
    <div class="tier" style="top:68px">
      <h2 class="tier-name">Guppy</h2>
      <ul class="skills" style="width:230px">
        <li>Fully submerges and retrieves object from under water</li>
        <li>Blows bubbles through nose and mouth</li>
        <li>Floats on stomach with support (10 seconds) floats on back with support (10 seconds)</li>
        <li>Assisted glide on stomach- no kicking</li>
        <li>Rolls from front to back and back to front with support</li>
        <li>Straight leg flutter kick on front and back (15 seconds) with support</li>
      </ul>
    </div>
    <div class="move-up" style="left:26px;top:244px"><span class="move-up-tag">Move-Up</span><p class="move-up-text">Must demonstrate straight flutter<br>kicks and float with support</p></div>

    <div class="art" role="img" aria-label="Illustration of a yellow and teal tadpole frog" style="left:217px;top:295px;width:87px;height:70px;background:linear-gradient(135deg,#f1e63e,#27bdb3)"></div>
    <div class="tier" style="top:296px;left:44px">
      <h2 class="tier-name">Tadpole</h2>
    </div>
    <div class="tier" style="top:344px">
      <ul class="skills" style="width:290px">
        <li>Floats on back unsupported (10 sec)</li>
        <li>Floats on stomach unsupported (10 sec)</li>
        <li>Launch glide on stomach with proper flutter kick unassited</li>
        <li>Launch glide on back with proper flutter kick unassited</li>
        <li>Push off and swim using combination of arm and leg actions for 10 feet on front and back</li>
        <li>Launch-roll to back float unsupported</li>
        <li>Jump in and float on the back</li>
      </ul>
    </div>
    <div class="move-up" style="left:26px;top:472px"><span class="move-up-tag">Move-Up</span><p class="move-up-text" style="line-height:11.5px">Must perform proper flutter kicks and glides<br>unsupported. Must jump in and float<br>on the back for 10 sec.</p></div>
  </section>

  <!-- Level III : Minnow / Goldfish / Catfish -->
  <section class="banner" style="left:745px;top:53px">
    <svg class="banner-bg" viewBox="0 0 318 530" aria-hidden="true">
      <path d="M0 0H318V2C250 58 205 72 159 72C105 72 55 50 0 4Z" fill="var(--teal)"/>
      <path d="M0 8C55 55 108 78 159 78C208 78 255 58 318 6" fill="none" stroke="var(--yellow)" stroke-width="3"/>
      <path d="M0 192C70 186 140 188 185 194" fill="none" stroke="var(--yellow)" stroke-width="3"/>
      <path d="M318 346V372H284Z" fill="var(--teal)"/>
      <path d="M0 342C90 334 200 336 318 344" fill="none" stroke="var(--yellow)" stroke-width="4"/>
      <path d="M120 530C180 522 250 520 318 516V530Z" fill="var(--yellow)"/>
    </svg>
    <div class="brand"><span class="brand-square"></span><span class="brand-name">Walter Brightley Fieldgrounds</span></div>

    <div class="art" role="img" aria-label="Illustration of a yellow and teal minnow" style="left:226px;top:52px;width:90px;height:30px;background:linear-gradient(90deg,#f2e43c,#17a9a4)"></div>
    <div class="tier" style="top:60px">
      <h2 class="tier-name">Minnow</h2>
      <ul class="skills compact" style="width:290px">
        <li>Proper streamline body position (on back and stomach) with flutter kick</li>
        <li>Kick on stomach, arms to side, roll to back float, big breath in, back to kick on stomach</li>
        <li>Correct front crawl arm motion with side breathing</li>
        <li>Correct backstroke arm motion</li>
        <li>Demonstrate basic front crawl</li>
        <li>Demonstrate basic backstroke</li>
        <li>Can exit pool independently (elbows and knees)</li>
      </ul>
    </div>
    <div class="move-up side" style="left:192px;top:150px"><span class="move-up-tag">Move-Up</span><p class="move-up-text">Must perform basic front crawl and backstroke. Must jump into deep water, float and kick to the side of the pool independently</p></div>

    <div class="tier" style="top:200px">
      <h2 class="tier-name">Goldfish</h2>
      <ul class="skills compact" style="width:170px">
        <li>One arm up one arm down on stomach then to back</li>
        <li>Streamline on front roll to streamline on back</li>
        <li>Basic rhythmic breathing</li>
        <li>Demonstrates proper front crawl</li>
        <li>Demonstrates proper backstroke</li>
        <li>Treading 1 minute</li>
        <li>Basic elementary backstroke</li>
        <li>Side flutter kick</li>
        <li>Streamline roll to side kick</li>
      </ul>
    </div>
    <div class="move-up side" style="left:192px;top:258px"><span class="move-up-tag">Move-Up</span><p class="move-up-text">Must complete deep water orientation, front crawl, and backstroke with stamina</p></div>
    <div class="art" role="img" aria-label="Illustration of a white and teal goldfish" style="left:170px;top:312px;width:72px;height:32px;background:linear-gradient(135deg,#f5f5f0,#34bcb4)"></div>

    <div class="tier" style="top:350px">
      <h2 class="tier-name">Catfish</h2>
      <ul class="skills compact" style="width:165px">
        <li>Tread water for 2 min continuously</li>
        <li>Front crawl with rhythmic breathing, fingertip entry, arm reach and body roll consistent and with stamina</li>
        <li>Catch-up stroke with alternate breathing every 3 counts</li>
        <li>Front crawl with alternate breathing and side flutter kick</li>
        <li>Double arm backstroke with pull</li>
        <li>Backstroke switch</li>
        <li>Sitting and kneeling dives with streamline position</li>
      </ul>
    </div>
    <div class="art" role="img" aria-label="Illustration of a yellow catfish with whiskers" style="left:228px;top:374px;width:90px;height:38px;background:linear-gradient(90deg,#f2e43c,#2fb8ae)"></div>
    <div class="move-up side" style="left:195px;top:428px"><span class="move-up-tag" style="margin-top:30px">Move-Up</span><p class="move-up-text" style="width:78px">Must perform advanced front crawl with fingertip entry and rhythmic breathing consistently and with stamina</p></div>
  </section>

  <!-- Level IV : Dolphin / Marlin / Barracuda -->
  <section class="banner" style="left:244px;top:616px">
    <svg class="banner-bg" viewBox="0 0 318 530" aria-hidden="true">
      <path d="M0 0H318V2C250 58 205 72 159 72C105 72 55 50 0 4Z" fill="var(--teal)"/>
      <path d="M0 8C55 55 108 78 159 78C208 78 255 58 318 6" fill="none" stroke="var(--yellow)" stroke-width="3"/>
      <path d="M0 220V232H30Z" fill="var(--teal)"/>
      <path d="M150 238C210 235 270 218 300 208" fill="none" stroke="var(--yellow)" stroke-width="4"/>
      <path d="M0 388C100 380 200 384 318 392" fill="none" stroke="var(--yellow)" stroke-width="4"/>
      <path d="M318 394V420L282 406Z" fill="var(--teal)"/>
      <path d="M0 524C100 516 220 516 318 524V530H0Z" fill="var(--teal)"/>
      <path d="M0 522C100 514 220 514 318 522" fill="none" stroke="var(--yellow)" stroke-width="2.5"/>
    </svg>
    <div class="brand"><span class="brand-square"></span><span class="brand-name">Walter Brightley Fieldgrounds</span></div>

    <div class="art" role="img" aria-label="Illustration of a leaping teal dolphin" style="left:224px;top:62px;width:76px;height:75px;background:linear-gradient(135deg,#3cc6bd,#f1e43c)"></div>
    <div class="tier" style="top:67px">
      <h2 class="tier-name">Dolphin</h2>
      <ul class="skills compact" style="width:155px">
        <li>15 deep water bobs</li>
        <li>Correct body position and roll for backstroke</li>
        <li>Basic whip kick on front</li>
        <li>Basic elementary backstroke</li>
        <li>Performs streamline position</li>
        <li>Can reverse direction on front and back</li>
        <li>Diving into deep end from standing position</li>
        <li>Assisted somersault from knees</li>
      </ul>
    </div>
    <div class="move-up side" style="left:186px;top:150px"><span class="move-up-tag">Move-Up</span><p class="move-up-text">Must perform advanced backstroke with still head and side to side body roll consistently and with stamina</p></div>

    <div class="art" role="img" aria-label="Illustration of a leaping blue and white marlin" style="left:206px;top:234px;width:97px;height:94px;background:linear-gradient(135deg,#2fbfb5,#e8ede8)"></div>
    <div class="tier" style="top:242px">
      <h2 class="tier-name">Marlin</h2>
      <ul class="skills compact" style="width:155px">
        <li>Proper elementary backstroke with timing and glide</li>
        <li>Proper whip kick on front and back</li>
        <li>Basic breaststroke arms</li>
        <li>Basic dolphin kick with body roll motion</li>
        <li>Basic sculling</li>
        <li>Open turns</li>
        <li>Somersault from wall or from standing position</li>
      </ul>
    </div>
    <div class="move-up side" style="left:186px;top:338px"><span class="move-up-tag">Move-Up</span><p class="move-up-text">Must peform proper whip kick on front and back, and proper elementary backstroke.</p></div>

    <div class="art" role="img" aria-label="Illustration of a long yellow and teal barracuda" style="left:173px;top:425px;width:133px;height:30px;background:linear-gradient(90deg,#2fb8ae,#f1e43c)"></div>
    <div class="tier" style="top:397px">
      <h2 class="tier-name">Barracuda</h2>
      <ul class="skills compact" style="width:155px">
        <li>Proper breaststroke arms</li>
        <li>Proper breaststroke timing</li>
        <li>Basic sidestroke</li>
        <li>Standing dive</li>
        <li>Prone glide into summersault</li>
        <li>Dophin kick with streamline</li>
        <li>Sculling on front with flutter kick</li>
      </ul>
    </div>
    <div class="move-up side" style="left:186px;top:462px"><span class="move-up-tag" style="margin-top:6px">Move-Up</span><p class="move-up-text">Must demonstrate full breaststroke with proper body/head positon with stamina</p></div>
  </section>

  <!-- Level V & VI : Shark / Orca -->
  <section class="banner" style="left:579px;top:616px">
    <svg class="banner-bg" viewBox="0 0 318 530" aria-hidden="true">
      <path d="M0 0H318V2C250 58 205 72 159 72C105 72 55 50 0 4Z" fill="var(--teal)"/>
      <path d="M0 8C55 55 108 78 159 78C208 78 255 58 318 6" fill="none" stroke="var(--yellow)" stroke-width="3"/>
      <path d="M318 250V312H250Z" fill="var(--teal)"/>
      <path d="M0 300C80 316 180 314 250 292" fill="none" stroke="var(--yellow)" stroke-width="3"/>
      <path d="M0 289V347L50 317Z" fill="var(--teal)"/>
      <path d="M0 338C120 324 230 294 318 236" fill="none" stroke="var(--yellow)" stroke-width="5"/>
      <path d="M0 526C100 516 220 516 318 526V530H0Z" fill="var(--teal)"/>
      <path d="M60 530C110 518 210 518 270 530Z" fill="var(--yellow)"/>
    </svg>
    <div class="brand"><span class="brand-square"></span><span class="brand-name">Walter Brightley Fieldgrounds</span></div>

    <div class="art" role="img" aria-label="Illustration of a yellow and teal shark" style="left:211px;top:83px;width:99px;height:63px;background:linear-gradient(135deg,#f1e43c,#2fb8ae)"></div>
    <div class="tier" style="top:92px">
      <h2 class="tier-name">Shark</h2>
      <ul class="skills" style="width:290px">
        <li>Proper front crawl with stamina</li>
        <li>Proper backstroke with stamina</li>
        <li>Proper breaststroke with stamina</li>
        <li>Proper elementary backstroke with stamina</li>
        <li>Proper timing for sidestroke</li>
        <li>Basic butterfly</li>
        <li>Intro to flip turns</li>
        <li>Retrieve object from deep end and swim on back for 10 yards</li>
      </ul>
    </div>
    <div class="move-up" style="left:20px;top:244px"><span class="move-up-tag" style="margin-top:10px">Move-Up</span><p class="move-up-text">Must perform proper front<br>crawl, backstroke, and<br>breaststroke with stamina<br>and basic butterfly</p></div>

    <div class="art" role="img" aria-label="Illustration of a leaping yellow and teal orca" style="left:217px;top:337px;width:87px;height:106px;background:linear-gradient(160deg,#2fb8ae,#f1e43c)"></div>
    <div class="tier" style="top:346px">
      <h2 class="tier-name">Orca</h2>
      <ul class="skills" style="width:190px">
        <li>Demonstrate proficiency in all strokes for 50 yds</li>
        <li>Proper butterfly</li>
        <li>Front crawl flip turn</li>
        <li>Backstroke flip turn</li>
        <li>Open turns</li>
        <li>Shallow standing dive</li>
      </ul>
    </div>
    <div class="move-up" style="left:20px;top:480px"><span class="move-up-tag" style="margin-top:3px">Move-Up</span><p class="move-up-text">Must demonstrate proficiency in<br>all strokes and turns</p></div>
  </section>

</main>
</body>
</html>
```